BFCM Creatives Theme

We are looking for an initial design for our BFCM campaign this year to set the theme for all other creatives for BFCM. We are an ecommerce brand selling Merino wool baby clothing. Our flagship product is the Cozy Nestling Drift Cocoon (see images).

We are starting with the request for an instagram post, announcing the sale (details below). This post should be 1080x1350 but also look appealing in the square grid. I've attached a basic brand card showing color palette, fonts, and logos. I will also attach some image options. We are looking for your creativity to shine while aligning with our branding and connecting with the customer. If you have a specific idea and are looking for a specific image please contact us.

Sale Details:
- 20% Off Sitewide
- 11.28.24 - 12.02.24
- Excluding giftcards and imperfects. No rainchecks.

```html
<!DOCTYPE html>
<html lang="en">
<head>
<meta charset="utf-8">
<title>fleecely – 20% Off Sitewide</title>
<link rel="stylesheet" href="https://fonts.googleapis.com/css2?family=Quicksand:wght@600;700&family=Andika:wght@700&display=swap">
<style>
  :root {
    --ink: #333637;
    --gold: #c6a84f;
    --slate: #7a8694;
    --paper: #f4f3f1;
    --paper-edge: #e9e8e6;
    --tile-border: #c9a955;
  }
  * { box-sizing: border-box; margin: 0; padding: 0; }
  html, body { width: 960px; height: 1200px; overflow: hidden; }
  body {
    background: radial-gradient(ellipse at 50% 45%, var(--paper) 55%, var(--paper-edge) 100%);
    position: relative;
    font-family: "Quicksand", sans-serif;
    color: var(--ink);
  }
  .corner-bands { position: absolute; inset: 0; width: 960px; height: 1200px; }
  .brand {
    position: absolute; top: 142px; left: 0; width: 960px;
    display: flex; justify-content: center; align-items: center; gap: 12px;
  }
  .brand-dot {
    width: 44px; height: 44px; border-radius: 50%;
    border: 3px solid var(--ink);
  }
  .brand-name {
    font-family: "Quicksand", sans-serif; font-weight: 700;
    font-size: 50px; line-height: 1; color: var(--ink);
  }
  .headline, .subhead, .dates {
    position: absolute; left: 0; width: 960px; text-align: center;
    font-family: "Quicksand", sans-serif; font-weight: 700; line-height: 1;
  }
  .headline { top: 200px; font-size: 210px; letter-spacing: -6px; color: var(--ink); }
  .subhead { top: 410px; font-size: 120px; letter-spacing: 3px; color: var(--gold); }
  .product-grid {
    position: absolute; top: 548px; left: 117px;
    display: grid; grid-template-columns: repeat(4, 164px);
    grid-auto-rows: 128px; column-gap: 13px; row-gap: 14px;
  }
  .product-tile {
    border: 2px solid var(--tile-border); border-radius: 9px;
  }
  .tile-stack   { background: linear-gradient(160deg, #c9b9a2, #b9a78c); }
  .tile-blue    { background: linear-gradient(90deg, #e8e8e8 20%, #6f97c4 45%, #6f97c4 60%, #e8e8e8 80%); }
  .tile-oat     { background: linear-gradient(180deg, #f2f1ee 30%, #d8cebf 70%, #e7e1d8); }
  .tile-sage    { background: linear-gradient(180deg, #f5f5f3 35%, #b4c4a0 65%, #eeeeea); }
  .tile-flatlay { background: linear-gradient(90deg, #f3eee9 25%, #f1c8c6 45%, #f1c8c6 60%, #f3eee9 80%); }
  .tile-pink    { background: linear-gradient(90deg, #dadada 20%, #f2c9c8 45%, #f2c9c8 60%, #dadada 80%); }
  .tile-stripe  { background: linear-gradient(90deg, #cfcfcf 20%, #e3e7dc 45%, #e3e7dc 60%, #cfcfcf 80%); }
  .tile-peek    { background: linear-gradient(180deg, #f6f6f6 40%, #5f87b8 62%, #f0f0f0 80%); }
  .dates { top: 836px; font-size: 102px; letter-spacing: -1px; color: var(--ink); }
  .rule {
    position: absolute; top: 939px; left: 81px; width: 773px; height: 2px;
    background: var(--ink);
  }
  .terms {
    position: absolute; left: 0; width: 960px; text-align: center;
    font-family: "Andika", sans-serif; font-weight: 700;
    font-size: 42px; line-height: 1.3; color: var(--ink);
    top: 948px;
  }
</style>
</head>
<body>
  <svg class="corner-bands" viewBox="0 0 960 1200" aria-hidden="true">
    <polygon points="0,0 300,0 930,166" fill="var(--slate)"/>
    <polygon points="345,0 960,0 960,162" fill="var(--gold)"/>
    <polygon points="0,1200 930,1067 390,1200" fill="var(--slate)"/>
    <polygon points="420,1200 960,1200 960,1062" fill="var(--gold)"/>
  </svg>

  <div class="brand">
    <span class="brand-dot"></span>
    <span class="brand-name">fleecely</span>
  </div>

  <h1 class="headline">20%OFF</h1>
  <h2 class="subhead">SITEWIDE</h2>

  <div class="product-grid">
    <div class="product-tile tile-stack" role="img" aria-label="Stack of folded patterned sleep sacks on a wooden stool"></div>
    <div class="product-tile tile-blue" role="img" aria-label="Baby lying in a crib wearing a blue printed sleep sack"></div>
    <div class="product-tile tile-oat" role="img" aria-label="Baby sitting on a rug in an oat-coloured sleep sack"></div>
    <div class="product-tile tile-sage" role="img" aria-label="Baby playing in a crib wearing a sage green sleep sack"></div>
    <div class="product-tile tile-flatlay" role="img" aria-label="Pink strawberry-print sleep sack laid flat with accessories"></div>
    <div class="product-tile tile-pink" role="img" aria-label="Baby in a crib wearing a pink strawberry-print sleep sack"></div>
    <div class="product-tile tile-stripe" role="img" aria-label="Baby in a crib wearing a pale striped sleep sack"></div>
    <div class="product-tile tile-peek" role="img" aria-label="Baby lying in a crib in a blue sleep sack peeking through the bars"></div>
  </div>

  <p class="dates">11.28.24–12.02.24</p>
  <div class="rule"></div>
  <p class="terms">Excluding giftcards and imperfects.<br>No rainchecks.</p>
</body>
</html>
```